Business Card Design Project

double sided, embossed, name & logo on front font sonsie one, back Name Maribel Stoddart, mobile 0468214093, Phone 76139584,
email maribel@brightwipe.com, use sysbols on the back for example an envelope for email, a telephone for phone number etc.symbol slate grey writing navy blue

Industry/Entity Type

Business

```html
<!DOCTYPE html>
<html lang="en">
<head>
<meta charset="utf-8">
<title>Maribel Stoddart – Business Card Back</title>
<link rel="stylesheet" href="https://fonts.googleapis.com/css2?family=Comic+Neue:wght@400;700&family=Kalam:wght@400;700&display=swap">
<style>
  :root {
    --card-bg: #ffffff;
    --ink-navy: #16136b;
    --icon-slate: #6d7478;
    --icon-light: #ffffff;
  }
  html, body {
    margin: 0;
    padding: 0;
    width: 1200px;
    height: 741px;
    overflow: hidden;
    background: var(--card-bg);
  }
  .card {
    position: relative;
    width: 1200px;
    height: 741px;
    background: var(--card-bg);
    overflow: hidden;
  }
  .card-name {
    position: absolute;
    right: 22px;
    top: 70px;
    margin: 0;
    font-family: "Comic Neue", "Comic Sans MS", cursive;
    font-weight: 700;
    font-size: 122px;
    line-height: 1;
    color: var(--ink-navy);
    letter-spacing: 1px;
    white-space: nowrap;
  }
  .contact-row {
    position: absolute;
    display: flex;
    align-items: center;
    font-family: "Kalam", "Comic Sans MS", cursive;
    font-weight: 700;
    color: var(--ink-navy);
    white-space: nowrap;
  }
  .contact-row svg { display: block; flex: none; }
  .contact-mobile {
    right: 34px;
    top: 250px;
    font-size: 50px;
    letter-spacing: 3px;
    gap: 22px;
  }
  .contact-phone {
    right: 72px;
    top: 322px;
    font-size: 50px;
    letter-spacing: 3px;
    gap: 44px;
  }
  .contact-email {
    right: 30px;
    top: 374px;
    font-size: 46px;
    letter-spacing: 0.5px;
    gap: 10px;
  }
  .contact-text { line-height: 1; }
</style>
</head>
<body>
  <main class="card">
    <h1 class="card-name">Maribel Stoddart</h1>

    <div class="contact-row contact-mobile">
      <svg width="32" height="52" viewBox="0 0 32 52" aria-hidden="true">
        <rect x="24" y="0" width="3" height="8" fill="var(--icon-slate)"/>
        <rect x="2" y="6" width="28" height="45" rx="4" fill="var(--icon-slate)"/>
        <rect x="6" y="11" width="20" height="17" fill="var(--icon-light)"/>
        <rect x="7" y="33" width="18" height="13" rx="1" fill="#a7adb0"/>
      </svg>
      <span class="contact-text">0468214093</span>
    </div>

    <div class="contact-row contact-phone">
      <svg width="58" height="38" viewBox="0 0 58 38" aria-hidden="true">
        <path d="M2 14 C2 4 56 4 56 14 L56 18 L44 18 L44 12 C38 10 20 10 14 12 L14 18 L2 18 Z" fill="var(--icon-slate)"/>
        <path d="M14 18 L44 18 L52 36 L6 36 Z" fill="var(--icon-slate)"/>
        <circle cx="29" cy="27" r="6" fill="var(--icon-light)"/>
        <circle cx="29" cy="27" r="2.5" fill="var(--icon-slate)"/>
      </svg>
      <span class="contact-text">76139584</span>
    </div>

    <div class="contact-row contact-email">
      <svg width="72" height="80" viewBox="0 0 72 80" aria-hidden="true">
        <path d="M2 28 L36 2 L70 28 L70 62 L2 62 Z" fill="var(--icon-slate)"/>
        <rect x="14" y="14" width="44" height="30" fill="var(--icon-light)"/>
        <path d="M2 28 L36 52 L70 28 L70 62 L2 62 Z" fill="var(--icon-slate)" stroke="var(--icon-light)" stroke-width="2.5"/>
        <path d="M2 62 L30 40 M70 62 L42 40" stroke="var(--icon-light)" stroke-width="2.5"/>
        <path d="M36 40 L36 70 L43 63 L49 76 L54 74 L48 61 L58 60 Z" fill="var(--icon-slate)" stroke="var(--icon-light)" stroke-width="2.5" stroke-linejoin="round"/>
      </svg>
      <span class="contact-text">maribel@brightwipe.com</span>
    </div>
  </main>
</body>
</html>
```